Brightwell Letterhead

We would like a letterhead for our company. I have uploaded our logo.

Brightwell Peak Consulting
1450 W Corvin Rd Ste 310
Arlington, TX 76006
844-555-0172

```html
<!DOCTYPE html>
<html lang="en">
<head>
<meta charset="utf-8">
<title>Brightwell Peak Consulting Letterhead</title>
<link href="https://fonts.googleapis.com/css2?family=Lato:wght@400;700&family=Open+Sans:wght@400;600&display=swap" rel="stylesheet">
<style>
  :root {
    --backdrop: #e9ebec;
    --paper: #ffffff;
    --ink: #4a4a4a;
    --ink-strong: #333333;
    --teal-dark: #16606c;
    --brand-teal: #1b5563;
    --mint: #5cc296;
    --mint-deep: #3f9a80;
  }
  * { margin: 0; padding: 0; box-sizing: border-box; }
  html, body { width: 1040px; height: 1200px; overflow: hidden; }
  body { background: var(--backdrop); position: relative; }

  .letterhead {
    position: absolute;
    left: 77px;
    top: 30px;
    width: 790px;
    height: 1017px;
    background: var(--paper);
    transform: scale(1.12);
    transform-origin: top left;
    box-shadow: 0 2px 6px rgba(0,0,0,0.12);
    overflow: hidden;
    font-family: "Open Sans", Arial, sans-serif;
    color: var(--ink);
  }

  .brand {
    position: absolute;
    top: 30px;
    right: 78px;
    display: flex;
    align-items: center;
    gap: 10px;
  }
  .brand-dot {
    width: 42px; height: 42px;
    border-radius: 50%;
    background: var(--brand-teal);
  }
  .brand-name {
    font-family: "Lato", Arial, sans-serif;
    font-weight: 700;
    color: var(--brand-teal);
    line-height: 1;
  }
  .brand-name .line-1 { display: block; font-size: 20px; letter-spacing: 1.5px; }
  .brand-name .line-2 { display: block; font-size: 16px; letter-spacing: 2px; margin-top: 4px; }

  .letter-body {
    position: absolute;
    left: 74px;
    top: 184px;
    width: 638px;
    font-size: 12.4px;
  }
  .issue-date { line-height: 16px; }
  .recipient { margin-top: 15px; line-height: 15px; }
  .salutation { margin-top: 44px; line-height: 16px; }
  .paragraph {
    margin-top: 22px;
    line-height: 23px;
    text-align: justify;
    hyphens: auto;
  }
  .closing { margin-top: 44px; line-height: 16px; }
  .signatory-name {
    margin-top: 50px;
    font-size: 15.5px;
    font-weight: 600;
    color: var(--ink-strong);
  }
  .signatory-title { margin-top: 3px; font-size: 12.4px; }

  .footer-band {
    position: absolute;
    left: 0; bottom: 0;
    width: 790px; height: 150px;
    background: linear-gradient(to bottom,
      var(--mint) 0,
      var(--mint-deep) 12px,
      var(--teal-dark) 30px,
      var(--teal-dark) 100%);
  }
  .footer-contact {
    position: absolute;
    left: 76px;
    top: 912px;
    font-family: "Lato", Arial, sans-serif;
    color: #ffffff;
  }
  .contact-row { display: flex; align-items: flex-start; gap: 6px; }
  .contact-row svg { flex: none; }
  .phone { font-size: 17px; line-height: 22px; }
  .address-row { margin-top: 8px; }
  .company-line { font-size: 15px; color: var(--mint); text-transform: uppercase; line-height: 18px; }
  .street-line { font-size: 15px; line-height: 19px; }
</style>
</head>
<body>
  <article class="letterhead">
    <header class="brand">
      <span class="brand-dot"></span>
      <span class="brand-name">
        <span class="line-1">BRIGHTWELL PEAK</span>
        <span class="line-2">CONSULTING</span>
      </span>
    </header>

    <section class="letter-body">
      <p class="issue-date">Issuing Date: May 5, 2018</p>
      <p class="recipient">Name Of Employee Mr. XYZABC<br>Address of Employee<br>Address Line 2 etc..</p>
      <p class="salutation">Dear Mr.XYZABC</p>
      <p class="paragraph">Lorem Ipsum has been the industry's standard dummy text ever since the 1500s, when an unknown printer took a galley of type and scrambled it to make a type specimen book. It has survived not only five centuries, but also the leap into electronic typesetting, remaining essentially unchanged. It was popularised in the 1960s with the release of Typeset sheets containing Lorem Ipsum passages, and more recently with desktop publishing software like Folio PageCraft including versions of Lorem Ipsum.</p>
      <p class="paragraph">Lorem Ipsum is simply dummy text of the printing and typesetting industry. Lorem Ipsum has been the industry's standard dummy text ever since the 1500s, when an unknown printer took a galley of type and scrambled it to make a type specimen book.</p>
      <p class="paragraph">It has survived not only five centuries, but also the leap into electronic typesetting, remaining essentially unchanged. It was popularised in the 1960s with the release of Typeset sheets containing Lorem IpsumIpsum passages.</p>
      <p class="closing">Yours Sincerely</p>
      <p class="signatory-name">Jonathan Reed</p>
      <p class="signatory-title">Managing Director</p>
    </section>

    <div class="footer-band" role="img" aria-label="Decorative footer band in mint and deep teal"></div>

    <footer class="footer-contact">
      <div class="contact-row">
        <svg width="16" height="18" viewBox="0 0 24 24" aria-hidden="true">
          <path d="M6.6 10.8a15.1 15.1 0 0 0 6.6 6.6l2.2-2.2a1 1 0 0 1 1-.25 11.4 11.4 0 0 0 3.6.57 1 1 0 0 1 1 1V20a1 1 0 0 1-1 1A17 17 0 0 1 3 4a1 1 0 0 1 1-1h3.5a1 1 0 0 1 1 1c0 1.25.2 2.45.57 3.57a1 1 0 0 1-.25 1z" fill="none" stroke="#5cc296" stroke-width="2"/>
        </svg>
        <span class="phone">844-555-0172</span>
      </div>
      <div class="contact-row address-row">
        <svg width="16" height="22" viewBox="0 0 24 32" aria-hidden="true">
          <path d="M12 1C6 1 2 5.5 2 11c0 7.5 10 20 10 20s10-12.5 10-20C22 5.5 18 1 12 1zm0 14a4 4 0 1 1 0-8 4 4 0 0 1 0 8z" fill="#5cc296"/>
        </svg>
        <div>
          <p class="company-line">Brightwell Peak Consulting</p>
          <p class="street-line">1450 W Corvin Rd Ste 310, Arlington, TX 76006</p>
        </div>
      </div>
    </footer>
  </article>
</body>
</html>
```